Classy, Elegant, Simple Business Card Design

Looking to have a classy, simple, and elegant design. Want a top notch designed business card. I really like the look of the new brivo credit card. I also like the design I attached. I am trying to reach 21-29 year old females for booking us for there wedding or event. We offer Disc Jockey Service, Photo Booth Rentals, and Uplighting .

Target Market(s)

21-28 year old females

Contact Information for Business Card

Has to have logo, website, email, and phone number

Font styles to use
Other font styles liked:
• open to font choice, modern, clean
Designer to choose
33a6d7
0791cd
0555a3
ffffff

Requirements
Must have
• Has to have logo, website, email, and phone number
Nice to have
• I really like the design of the new brivo credit card. I also included my logo and some designs I like
Should not have
• clutter or too much info

```html
<!DOCTYPE html>
<html lang="en">
<head>
<meta charset="utf-8">
<title>Tidewell Event Group – Business Card</title>
<link rel="stylesheet" href="https://fonts.googleapis.com/css2?family=Didact+Gothic&family=Open+Sans:wght@400;600&display=swap">
<style>
  :root {
    --backdrop: #d9dbde;
    --card-navy: #0f2c55;
    --card-navy-deep: #0c2549;
    --sky: #33a6d7;
    --azure: #0791cd;
    --royal: #0555a3;
    --white: #ffffff;
    --shadow: rgba(10, 20, 40, 0.35);
  }
  * { box-sizing: border-box; margin: 0; padding: 0; }
  html, body {
    width: 1200px; height: 1021px; overflow: hidden;
    background: var(--backdrop);
  }
  .canvas {
    position: relative; width: 1200px; height: 1021px;
  }
  .card {
    position: absolute; left: 220px; width: 760px; height: 434px;
    background: linear-gradient(135deg, var(--card-navy) 0%, var(--card-navy-deep) 100%);
    box-shadow: 0 14px 30px var(--shadow);
    color: var(--white);
    font-family: "Open Sans", sans-serif;
  }
  .card--front { top: 52px; }
  .card--back { top: 535px; }

  .wordmark {
    display: flex; align-items: center; gap: 14px;
    font-family: "Didact Gothic", sans-serif;
    color: var(--white);
    letter-spacing: 0.08em;
  }
  .wordmark__dot {
    flex: none; border-radius: 50%; background: var(--sky);
  }
  .card--front .wordmark {
    position: absolute; left: 50%; top: 50%;
    transform: translate(-50%, -50%);
    font-size: 44px;
  }
  .card--front .wordmark__dot { width: 22px; height: 22px; }

  .card--back .wordmark {
    position: absolute; left: 56px; top: 52px;
    font-size: 30px;
  }
  .card--back .wordmark__dot { width: 16px; height: 16px; }

  .contact {
    position: absolute; left: 56px; top: 140px;
    font-size: 19px; line-height: 1.4;
  }
  .contact__address { margin-bottom: 14px; }
  .contact__line {
    display: flex; align-items: center; gap: 10px;
  }
  .contact__icon { width: 18px; height: 18px; flex: none; }

  .person {
    position: absolute; right: 64px; bottom: 58px; text-align: right;
  }
  .person__name {
    color: var(--azure); font-weight: 600; font-size: 26px;
  }
  .person__role { font-size: 20px; margin-top: 2px; }
</style>
</head>
<body>
<main class="canvas">

  <section class="card card--front" aria-label="Card front">
    <div class="wordmark">
      <span class="wordmark__dot"></span>
      <span class="wordmark__name">TIDEWELL EVENT GROUP</span>
    </div>
  </section>

  <section class="card card--back" aria-label="Card back">
    <div class="wordmark">
      <span class="wordmark__dot"></span>
      <span class="wordmark__name">TIDEWELL EVENT GROUP</span>
    </div>

    <div class="contact">
      <p class="contact__address">48 Harbor Lane, Suite 310<br>Coral Bay, Florida, 33140</p>
      <p class="contact__line">
        <svg class="contact__icon" viewBox="0 0 24 24" aria-hidden="true">
          <path fill="#33a6d7" d="M6.6 10.8a15.1 15.1 0 0 0 6.6 6.6l2.2-2.2a1 1 0 0 1 1-.25 11.4 11.4 0 0 0 3.6.57 1 1 0 0 1 1 1V20a1 1 0 0 1-1 1A17 17 0 0 1 3 4a1 1 0 0 1 1-1h3.5a1 1 0 0 1 1 1c0 1.25.2 2.45.57 3.6a1 1 0 0 1-.25 1z"/>
        </svg>
        (555) 218-4471
      </p>
      <p class="contact__line">
        <svg class="contact__icon" viewBox="0 0 24 24" aria-hidden="true">
          <rect x="2.5" y="5" width="19" height="14" fill="none" stroke="#33a6d7" stroke-width="2"/>
          <path d="M3 6l9 7 9-7" fill="none" stroke="#33a6d7" stroke-width="2"/>
        </svg>
        daniel@tidewellevents.com
      </p>
      <p class="contact__line">
        <svg class="contact__icon" viewBox="0 0 24 24" aria-hidden="true">
          <circle cx="12" cy="12" r="9.5" fill="none" stroke="#33a6d7" stroke-width="2"/>
          <ellipse cx="12" cy="12" rx="4" ry="9.5" fill="none" stroke="#33a6d7" stroke-width="1.6"/>
          <path d="M2.5 12h19M4.5 7h15M4.5 17h15" stroke="#33a6d7" stroke-width="1.6"/>
        </svg>
        www.tidewellevents.com
      </p>
    </div>

    <div class="person">
      <p class="person__name">Daniel Reyes</p>
      <p class="person__role">Founder</p>
    </div>
  </section>

</main>
</body>
</html>
```